Eye catching Stationary Design

Healthcare consultant firm looking for stationary design ( letterhead, envelope and business cards) That’s professional, classy and eye catching . The design should incorporate the logo and the colors of the logo in its design. You can see the logo on our website at www crestmore advisory. net.

```html
<!DOCTYPE html>
<html lang="en">
<head>
<meta charset="utf-8">
<title>Crestmore Advisory – Stationery Set</title>
<link href="https://fonts.googleapis.com/css2?family=Arimo:wght@400;700&display=swap" rel="stylesheet">
<style>
  :root {
    --backdrop: #c3c3c3;
    --paper: #ffffff;
    --ink: #1b1b1b;
    --brand-dark: #0055a5;
    --brand-light: #2ea3d5;
    --rule: #2b9fd9;
    --night: #0f1214;
  }
  * { margin: 0; padding: 0; box-sizing: border-box; }
  html, body { width: 1200px; height: 1200px; overflow: hidden; }
  body {
    position: relative;
    background: var(--backdrop);
    font-family: "Arimo", Arial, sans-serif;
    color: var(--ink);
  }
  .sheet {
    position: absolute;
    background: var(--paper);
    box-shadow: 2px 3px 6px rgba(0,0,0,.35);
    overflow: hidden;
  }
  .band { position: absolute; left: 0; bottom: 0; width: 100%; display: block; }
  .brand-name {
    position: absolute;
    color: var(--brand-dark);
    font-weight: 700;
    white-space: nowrap;
    text-transform: uppercase;
    letter-spacing: .04em;
    line-height: 1;
  }
  .blue { color: var(--brand-dark); }

  /* Letterhead */
  .letterhead { left: 12px; top: 95px; width: 785px; height: 1009px; }
  .letterhead .brand-name { left: 0; width: 100%; text-align: center; top: 110px; font-size: 21px; }
  .letterhead .rule { position: absolute; left: 64px; width: 663px; height: 1.5px; background: var(--rule); }
  .letterhead .rule.top { top: 150px; }
  .letterhead .rule.bottom { top: 903px; }
  .letterhead .contacts { position: absolute; left: 62px; top: 922px; font-size: 15.5px; line-height: 20px; }
  .letterhead .address { position: absolute; right: 58px; top: 922px; font-size: 15.5px; line-height: 20px; text-align: right; }
  .contacts li { list-style: none; display: flex; align-items: center; gap: 7px; }
  .contacts svg { flex: none; }

  /* Envelope front */
  .envelope-front { left: 814px; top: 200px; width: 369px; height: 160px; }
  .envelope-front .brand-name { left: 22px; top: 48px; font-size: 8px; }
  .envelope-front .return { position: absolute; left: 22px; top: 126px; padding-left: 7px; border-left: 1px solid var(--rule); font-size: 6.5px; line-height: 9.5px; }

  /* Envelope back */
  .envelope-back { left: 814px; top: 392px; width: 369px; height: 159px; }
  .envelope-back .flap { position: absolute; left: 0; top: 0; width: 369px; height: 60px; display: block; }
  .envelope-back .brand-name { left: 0; width: 100%; text-align: center; top: 28px; font-size: 6px; color: var(--brand-light); }
  .envelope-back .web { position: absolute; left: 0; width: 100%; text-align: center; top: 136px; font-size: 6.5px; }

  /* Business card front */
  .card-front { left: 818px; top: 629px; width: 301px; height: 173px; }
  .card-front .brand-name { left: 0; width: 100%; text-align: center; top: 50px; font-size: 9.5px; }
  .card-front .person { position: absolute; left: 0; width: 100%; text-align: center; top: 89px; }
  .card-front .person-name { font-size: 12px; color: var(--brand-dark); font-weight: 400; }
  .card-front .person-role { font-size: 7px; margin-top: 1px; }
  .card-front .rule { position: absolute; left: 22px; width: 258px; top: 119px; height: 1px; background: var(--rule); }
  .card-front .contacts { position: absolute; left: 22px; top: 128px; font-size: 7px; line-height: 10.3px; }
  .card-front .contacts li { gap: 4px; }
  .card-front .address { position: absolute; right: 21px; top: 128px; font-size: 7px; line-height: 10.3px; text-align: right; }

  /* Business card back */
  .card-back { left: 818px; top: 826px; width: 301px; height: 173px; background: var(--night); }
  .card-back .brand-name { left: 0; width: 100%; text-align: center; top: 103px; font-size: 11.5px; color: var(--brand-light); }
  .card-back .web { position: absolute; left: 0; width: 100%; text-align: center; top: 146px; font-size: 7px; color: #e6e6e6; }
  .card-back .web .blue { color: var(--brand-light); }
</style>
</head>
<body>

  <!-- Letterhead -->
  <section class="sheet letterhead">
    <div class="brand-name">Crestmore Advisory LLC</div>
    <div class="rule top"></div>
    <div class="rule bottom"></div>
    <ul class="contacts">
      <li>
        <svg width="14" height="14" viewBox="0 0 24 24"><path fill="#0055a5" d="M6.6 10.8a15 15 0 0 0 6.6 6.6l2.2-2.2c.3-.3.7-.4 1-.2 1.1.4 2.3.6 3.6.6.6 0 1 .4 1 1V20c0 .6-.4 1-1 1A17 17 0 0 1 3 4c0-.6.4-1 1-1h3.5c.6 0 1 .4 1 1 0 1.3.2 2.5.6 3.6.1.3 0 .7-.2 1z"/></svg>
        (555) 014-2290
      </li>
      <li>
        <svg width="14" height="14" viewBox="0 0 24 24"><rect x="2" y="5" width="20" height="14" fill="#0055a5"/><path d="M2 5l10 8 10-8M2 19l7-7M22 19l-7-7" stroke="#fff" stroke-width="1.6" fill="none"/></svg>
        info@crestmoreadvisory.net
      </li>
      <li>
        <svg width="14" height="14" viewBox="0 0 24 24" fill="none" stroke="#0055a5" stroke-width="1.8"><circle cx="12" cy="12" r="9.5"/><ellipse cx="12" cy="12" rx="4" ry="9.5"/><path d="M2.5 12h19M4 7h16M4 17h16"/></svg>
        <span>www.<span class="blue">crestmoreadvisory</span>.net</span>
      </li>
    </ul>
    <div class="address">180 Harbor Ln S12<br>Eastfield<br>NY 10999, USA</div>
    <svg class="band" height="16" viewBox="0 0 785 16" preserveAspectRatio="none">
      <polygon points="0,0 400,0 385,16 0,16" fill="var(--brand-dark)"/>
      <polygon points="413,0 785,0 785,16 398,16" fill="var(--brand-light)"/>
    </svg>
  </section>

  <!-- Envelope front -->
  <section class="sheet envelope-front">
    <div class="brand-name">Crestmore Advisory LLC</div>
    <div class="return">180 Harbor Ln S12<br>Eastfield, NY 10999, USA</div>
    <svg class="band" height="6" viewBox="0 0 369 6" preserveAspectRatio="none">
      <polygon points="0,0 189,0 184,6 0,6" fill="var(--brand-dark)"/>
      <polygon points="192,0 369,0 369,6 187,6" fill="var(--brand-light)"/>
    </svg>
  </section>

  <!-- Envelope back -->
  <section class="sheet envelope-back">
    <svg class="flap" viewBox="0 0 369 60">
      <path d="M0 0H369L362 36Q358 47 346 47H23Q11 47 7 36Z" fill="var(--night)"/>
    </svg>
    <svg style="position:absolute;left:0;top:47px" width="369" height="106" viewBox="0 0 369 106">
      <path d="M12 0L1 103M357 0L368 103" stroke="#b8b8b8" stroke-width=".7" fill="none"/>
    </svg>
    <div class="brand-name">Crestmore Advisory LLC</div>
    <div class="web">www.<span class="blue">crestmoreadvisory</span>.net</div>
    <svg class="band" height="6" viewBox="0 0 369 6" preserveAspectRatio="none">
      <polygon points="0,0 189,0 184,6 0,6" fill="var(--brand-dark)"/>
      <polygon points="192,0 369,0 369,6 187,6" fill="var(--brand-light)"/>
    </svg>
  </section>

  <!-- Business card front -->
  <section class="sheet card-front">
    <div class="brand-name">Crestmore Advisory LLC</div>
    <div class="person">
      <div class="person-name">Jordan Ellis</div>
      <div class="person-role">Owner</div>
    </div>
    <div class="rule"></div>
    <ul class="contacts">
      <li>
        <svg width="7" height="7" viewBox="0 0 24 24"><path fill="#0055a5" d="M6.6 10.8a15 15 0 0 0 6.6 6.6l2.2-2.2c.3-.3.7-.4 1-.2 1.1.4 2.3.6 3.6.6.6 0 1 .4 1 1V20c0 .6-.4 1-1 1A17 17 0 0 1 3 4c0-.6.4-1 1-1h3.5c.6 0 1 .4 1 1 0 1.3.2 2.5.6 3.6.1.3 0 .7-.2 1z"/></svg>
        (555) 014-2290
      </li>
      <li>
        <svg width="7" height="7" viewBox="0 0 24 24"><rect x="2" y="5" width="20" height="14" fill="#0055a5"/><path d="M2 5l10 8 10-8" stroke="#fff" stroke-width="2" fill="none"/></svg>
        info@crestmoreadvisory.net
      </li>
      <li>
        <svg width="7" height="7" viewBox="0 0 24 24" fill="none" stroke="#0055a5" stroke-width="2.2"><circle cx="12" cy="12" r="9.5"/><ellipse cx="12" cy="12" rx="4" ry="9.5"/><path d="M2.5 12h19"/></svg>
        <span>www.<span class="blue">crestmoreadvisory</span>.net</span>
      </li>
    </ul>
    <div class="address">180 Harbor Ln S12<br>Eastfield<br>NY 10999, USA</div>
    <svg class="band" height="6" viewBox="0 0 301 6" preserveAspectRatio="none">
      <polygon points="0,0 151,0 146,6 0,6" fill="var(--brand-dark)"/>
      <polygon points="154,0 301,0 301,6 149,6" fill="var(--brand-light)"/>
    </svg>
  </section>

  <!-- Business card back -->
  <section class="sheet card-back">
    <div class="brand-name">Crestmore Advisory LLC</div>
    <div class="web">www.<span class="blue">crestmoreadvisory</span>.net</div>
    <svg class="band" height="6" viewBox="0 0 301 6" preserveAspectRatio="none">
      <polygon points="0,0 151,0 146,6 0,6" fill="var(--brand-dark)"/>
      <polygon points="154,0 301,0 301,6 149,6" fill="var(--brand-light)"/>
    </svg>
  </section>

</body>
</html>
```